Static landing page for our consulting business

Hi

I require a website for a company called "Quenlo (Pty) Ltd"
It is a management consulting company with three core consulting services.
1. IT
2. Finance
3. Engineering

Our webpage basically needs a landing page with an overview and history of the company.

Then a sub section for each of the three disciplines with a description of what services are rendered. Each of these sections needs to have a link to the consultant that heads up that discipline.

Each consultant of which there are 3 potentially four shortly then needs a page that could introduce themselves, their qualifications etc.

There would also be a 'contact us & information page'
I have attached company logo for your reference.

Target Market(s)

Finance and management consulting

Industry/Entity Type

Business

Coding

Coded - Design and coding required

Number of Pages Required

1 page

Font styles to use
Sans Serif

Colors
33a6d7
85cae6
f68d4d
0492cd
f37122

Requirements
Must have
• basic html page with CSS, no back end or .net. Would run on a php server, and we would add the dynamic content ourselves if required later.
Nice to have
• Social media links, we would code them later.

```html
<!DOCTYPE html>
<html lang="en">
<head>
<meta charset="utf-8">
<title>Quenlo (Pty) Ltd — Management Consulting</title>
<link rel="stylesheet" href="https://fonts.googleapis.com/css2?family=Oswald:wght@300;400;500&family=Open+Sans:wght@400;600;700&display=swap">
<style>
:root{
  --blue:#0492cd;
  --blue-mid:#33a6d7;
  --blue-light:#85cae6;
  --orange:#f37122;
  --orange-light:#f68d4d;
  --navy:#1d2f44;
  --ink:#333;
  --muted:#555;
  --peach:#fde6d7;
  --footer:#0b0b0b;
  --footer-bar:#2a2a2a;
}
*{box-sizing:border-box;margin:0;padding:0}
html,body{width:1200px;height:2692px;overflow:hidden}
body{font-family:"Open Sans",Arial,sans-serif;color:var(--ink);background:#fff;position:relative}
.heading{font-family:"Oswald",Arial,sans-serif;font-weight:400;color:var(--blue);text-align:center;font-size:44px}
.copy{font-size:14px;line-height:22px;color:var(--muted);text-align:center;width:1000px;margin:0 auto}

/* header */
.site-header{position:absolute;top:0;left:0;width:1200px;height:128px;background:#fff}
.brand{position:absolute;left:92px;top:30px;font-family:"Open Sans",Arial,sans-serif;font-weight:700;font-size:34px;line-height:40px;color:var(--navy);width:200px}
.brand small{display:block;font-size:20px;line-height:24px}
.brand-mark{position:absolute;left:-22px;top:8px;width:14px;height:14px;background:var(--orange);border-radius:50%}
.socials{position:absolute;left:690px;top:10px;display:flex;gap:8px}
.socials span{width:20px;height:20px;background:var(--blue);display:block}
.quote-btn{position:absolute;right:96px;top:4px;width:140px;height:30px;background:var(--blue);color:#fff;font-size:12px;line-height:30px;text-align:center}
.main-nav{position:absolute;left:406px;top:64px;display:flex;align-items:center;gap:30px;font-size:14px;color:var(--ink)}
.home-icon{width:30px;height:30px;background:var(--blue);display:flex;align-items:center;justify-content:center}
.main-nav a{color:var(--ink);text-decoration:none}
.phone{position:absolute;right:96px;top:68px;display:flex;align-items:center;gap:8px;font-size:14px;color:var(--ink)}

/* hero */
.hero{position:absolute;top:128px;left:0;width:1200px;height:512px;background:linear-gradient(120deg,#2c3e56 0%,#4c6784 45%,#8aa2b8 75%,#c9d5df 100%)}
.hero-text{position:absolute;left:500px;top:80px;width:400px;font-family:"Oswald",Arial,sans-serif;color:#fff}
.hero-text .l1{font-weight:300;font-size:62px;line-height:70px}
.hero-text .l2{font-weight:500;font-size:66px;line-height:72px}
.hero-text .l3{font-weight:300;font-size:36px;line-height:44px;text-align:center;width:320px}
.hero-btn{position:absolute;left:620px;top:344px;width:120px;height:38px;background:var(--blue);color:#fff;font-size:12px;line-height:38px;text-align:center}

/* about */
.about{position:absolute;top:640px;left:0;width:1200px;height:280px}
.about .heading{margin-top:64px}
.about .copy{margin-top:26px}

.service-strip{position:absolute;top:920px;left:0;width:1200px;height:130px;background:linear-gradient(90deg,#9fb3c3,#d7dee4 30%,#5c7690 55%,#c4ced6 80%,#8fa4b5)}
.service-band{position:absolute;top:1050px;left:0;width:1200px;height:450px;background:linear-gradient(180deg,#0f7fb8 0%,#33a6d7 45%,#85cae6 100%)}
.service-cards{position:absolute;top:1072px;left:144px;display:flex;gap:8px}
.service-card{width:300px;height:176px;background:#fff;padding:24px 22px;text-align:center}
.service-card.featured{background:var(--peach)}
.service-card h3{font-family:"Oswald",Arial,sans-serif;font-weight:400;font-size:24px;color:var(--ink);margin-bottom:16px}
.service-card p{font-size:13px;line-height:20px;color:var(--muted)}

.specialists{position:absolute;top:1258px;left:144px;width:916px}
.specialists h2{font-family:"Oswald",Arial,sans-serif;font-weight:400;font-size:26px;color:#fff;text-align:center;margin-bottom:8px}
.specialist-box{background:#fff;height:134px;display:flex;justify-content:space-between;padding:24px 26px}
.specialist{display:flex;gap:14px;width:270px}
.avatar{width:84px;height:84px;background:linear-gradient(160deg,#9aa7b3,#566574)}
.specialist h4{font-family:"Oswald",Arial,sans-serif;font-weight:400;font-size:24px;color:var(--orange);line-height:30px}
.specialist p{font-size:12px;color:var(--muted);margin-bottom:8px}
.profile-btn{display:inline-block;background:var(--blue);color:#fff;font-size:11px;padding:5px 14px}

/* projects */
.projects{position:absolute;top:1560px;left:0;width:1200px}
.projects .heading{margin-top:40px}
.projects .copy{margin-top:26px}
.project-gallery{position:absolute;top:1838px;left:0;width:1200px;height:242px;display:flex;gap:6px}
.project-gallery div{flex:1}

/* contact */
.get-in-touch{position:absolute;top:2080px;left:0;width:1200px;height:312px;background:linear-gradient(180deg,#f4f4f4,#e2e4e6)}
.get-in-touch .heading{margin-top:72px}
.get-in-touch .copy{margin-top:26px}

.site-footer{position:absolute;top:2392px;left:0;width:1200px;height:248px;background:var(--footer);display:flex;padding:48px 0 0 176px;gap:0}
.footer-col{width:348px;color:#ddd;font-size:14px;line-height:20px}
.footer-col h5{font-family:"Oswald",Arial,sans-serif;font-weight:400;font-size:28px;color:#fff;margin-bottom:22px}
.footer-bar{position:absolute;top:2640px;left:0;width:1200px;height:52px;background:var(--footer-bar);color:#aaa;font-size:12px;text-align:center;line-height:52px}
</style>
</head>
<body>

<header class="site-header">
  <div class="brand"><span class="brand-mark"></span>Quenlo <small>(Pty) Ltd</small></div>
  <div class="socials"><span></span><span></span><span></span><span></span><span></span></div>
  <div class="quote-btn">Request a Quote</div>
  <nav class="main-nav">
    <span class="home-icon"><svg width="16" height="14" viewBox="0 0 16 14"><path d="M8 0 0 7h2v7h4V9h4v5h4V7h2z" fill="#fff"/></svg></span>
    <a href="#">About Us</a><a href="#">Our Projects</a><a href="#">Clients</a><a href="#">Contact</a>
  </nav>
  <div class="phone"><svg width="16" height="16" viewBox="0 0 16 16"><path d="M3 1l3 3-2 2c1 2 3 4 5 5l2-2 3 3-2 3C6 14 2 10 1 3z" fill="var(--blue)"/></svg>000 - 123 - 456 - 780</div>
</header>

<section class="hero" role="img" aria-label="Blueprint drawings with drafting tools on a desk">
  <div class="hero-text">
    <div class="l1">DISCOVER</div>
    <div class="l2">A BETTER WAY</div>
    <div class="l3">ONE STOP SERVICES</div>
  </div>
  <div class="hero-btn">Learn more</div>
</section>

<section class="about">
  <h2 class="heading">About Us</h2>
  <p class="copy">We are a management consulting firm helping businesses grow through clear advice in technology, finance and engineering. Since our founding we have worked beside clients of every size to plan, build and improve the systems that keep their operations steady, their costs in check and their teams focused on lasting results for the years ahead.</p>
</section>

<div class="service-strip" role="img" aria-label="Photo strip of computer hardware, financial documents and engineering work"></div>
<div class="service-band"></div>
<div class="service-cards">
  <div class="service-card"><h3>INFORMATION TECHNOLOGY</h3><p>Systems reviews, security planning and digital strategy that help your business work smarter every day.</p></div>
  <div class="service-card featured"><h3>FINANCIAL</h3><p>Budgeting, reporting and financial planning advice that gives you a clear view of where you stand.</p></div>
  <div class="service-card"><h3>ENGINEERING</h3><p>Project oversight, design reviews and process guidance that keep every build safe, sound and on time.</p></div>
</div>

<section class="specialists">
  <h2>Our Specialist</h2>
  <div class="specialist-box">
    <div class="specialist"><div class="avatar" role="img" aria-label="Portrait photo of the IT specialist"></div><div><h4>John Doe</h4><p>IT Expert &amp; Specialist</p><span class="profile-btn">View Profile</span></div></div>
    <div class="specialist"><div class="avatar" role="img" aria-label="Portrait photo of the financial specialist"></div><div><h4>John Doe</h4><p>Financial Specialist</p><span class="profile-btn">View Profile</span></div></div>
    <div class="specialist"><div class="avatar" role="img" aria-label="Portrait photo of the engineering specialist"></div><div><h4>John Doe</h4><p>Engineering Specialist</p><span class="profile-btn">View Profile</span></div></div>
  </div>
</section>

<section class="projects">
  <h2 class="heading">Our Projects</h2>
  <p class="copy">Our recent work spans bridges, port facilities, office networks and finance teams across the region. Each project starts with careful listening and ends with a measurable improvement our clients can see. Browse a few highlights below to learn how we plan, deliver and support work of every scale and kind.</p>
</section>
<div class="project-gallery">
  <div role="img" aria-label="Boat lift bridge over a canal" style="background:linear-gradient(180deg,#6f9fc6,#3f6a8c)"></div>
  <div role="img" aria-label="Harbour with ships at dusk" style="background:linear-gradient(180deg,#4c7ea0,#1f3f58)"></div>
  <div role="img" aria-label="Server room with network equipment" style="background:linear-gradient(180deg,#5a6f86,#1d2a3a)"></div>
  <div role="img" aria-label="Office worker at a computer desk" style="background:linear-gradient(180deg,#dfe5ea,#8fa0ae)"></div>
  <div role="img" aria-label="Business meeting in an office" style="background:linear-gradient(180deg,#e6e9ec,#6c7c8a)"></div>
</div>

<section class="get-in-touch">
  <h2 class="heading">Get Intouch</h2>
  <p class="copy">Have a question about our services or want to book a first meeting with one of our specialists? Send us a message or call during office hours and a member of our team will be glad to help you find the right next step.</p>
</section>

<footer class="site-footer">
  <div class="footer-col"><h5>CONTACT ADDRESS</h5>Building Address<br>Street Address<br>State, Country</div>
  <div class="footer-col"><h5>CONTACT DETAILS</h5>000-123-456-780<br>support@domain.com</div>
  <div class="footer-col"><h5>OFFICE HOURS</h5>9:00 am to 6pm<br>Monday to Friday</div>
</footer>
<div class="footer-bar">Copyright © 2015 Your Company Name</div>

</body>
</html>
```